Brochure template design

We would like to create a brochure temple for a trifold brochure.

This link has a photos and logos that can be used
https://www.filecrate-share.net/sh/qm4tz81kp0vhw2d/BBKpLeRtaYw-nJqVc_ZsdekTo?dl=0

the link also has our latest promotional video which will give you info on our company.

The style of the brochure should be in line with either our promotional video or our website www.harbourlanetrips.com.au

We would also ask the successfull designer to design a variety of other similar templates

Industry/Entity Type

It Company

Requirements
Must have
• our logo

```html
<!DOCTYPE html>
<html lang="en">
<head>
<meta charset="utf-8">
<title>Harbour Lane Trips – Trifold Brochure</title>
<link rel="stylesheet" href="https://fonts.googleapis.com/css2?family=Montserrat:wght@800&family=Open+Sans:wght@400;700&display=swap">
<style>
  :root {
    --stage: #0d0d0d;
    --navy: #25398a;
    --yellow: #f4e41c;
    --lime: #a6d23a;
    --green: #5fb946;
    --sky-text: #62c7f2;
    --white: #ffffff;
    --heading: "Montserrat", sans-serif;
    --body: "Open Sans", sans-serif;
  }
  * { box-sizing: border-box; margin: 0; padding: 0; }
  html, body { width: 900px; height: 1200px; overflow: hidden; }
  body {
    background: radial-gradient(ellipse at center, #2a2a2a 0%, var(--stage) 70%);
    position: relative;
    font-family: var(--body);
  }
  .brochure {
    position: absolute;
    left: 45px;
    width: 810px;
    height: 500px;
    box-shadow: 0 18px 40px rgba(0,0,0,.7);
    overflow: hidden;
    background: var(--navy);
  }
  .brochure--outside { top: 50px; }
  .brochure--inside { top: 640px; }
  .panel {
    position: absolute;
    top: 0;
    width: 270px;
    height: 500px;
    overflow: hidden;
  }
  .panel--1 { left: 0; }
  .panel--2 { left: 270px; }
  .panel--3 { left: 540px; }
  .panel + .panel { border-left: 1px solid rgba(0,0,0,.18); }

  .block { position: absolute; left: 0; width: 100%; }
  .block--navy { background: var(--navy); }
  .photo { position: absolute; left: 0; width: 100%; }

  .photo--surfer { top: 235px; height: 265px; background: linear-gradient(170deg, #6aa9e0 0%, #9ccdf0 35%, #e8f2f7 60%, #7da9c4 100%); }
  .photo--kayaks { top: 0; height: 260px; background: linear-gradient(180deg, #f6d9a0 0%, #f1b86a 25%, #8aa3b3 55%, #3c4550 100%); }
  .photo--climber { top: 275px; height: 225px; background: linear-gradient(160deg, #8fa06a 0%, #a7a59a 45%, #6f7467 100%); }
  .photo--cliff-group { top: 0; height: 250px; background: linear-gradient(180deg, #4f86c9 0%, #b5714f 35%, #8a5a3f 60%, #4d5b3a 100%); }
  .photo--beach-group { top: 270px; height: 230px; background: linear-gradient(180deg, #cfe3f2 0%, #b9d4e6 40%, #d9c7a4 70%, #cbb48e 100%); }
  .photo--raft { top: 0; height: 240px; background: linear-gradient(180deg, #9fc6ea 0%, #c7dcea 30%, #5d8a5a 45%, #4f8ea0 70%, #3c7285 100%); }

  .cover-top {
    top: 0; height: 275px;
    background: linear-gradient(180deg, #ffffff 0%, #f4f8fc 60%, #cfe3f4 100%);
  }
  .brand {
    position: absolute;
    left: 28px; top: 60px;
    display: flex; align-items: center; gap: 12px;
  }
  .brand__mark { width: 46px; height: 46px; background: var(--navy); flex: none; }
  .brand__name {
    font-family: var(--body);
    font-weight: 700;
    font-size: 27px;
    line-height: 1.05;
    color: var(--navy);
  }

  .copy {
    position: absolute;
    left: 24px; right: 22px;
    color: var(--white);
    font-size: 7px;
    line-height: 1.3;
  }
  .copy p + p { margin-top: 6px; }
  .copy ol { list-style: none; margin-top: 6px; }
  .levels { color: var(--sky-text); }

  .heading {
    display: flex; align-items: flex-start; gap: 8px;
    font-family: var(--heading);
    font-weight: 800;
    color: var(--yellow);
    font-size: 15px;
    line-height: 1.05;
    text-transform: uppercase;
    margin-bottom: 8px;
  }
  .heading svg { flex: none; margin-top: 2px; }
  .heading--center { justify-content: center; }

  .wave { position: absolute; left: 0; top: 0; width: 810px; height: 500px; pointer-events: none; }
</style>
</head>
<body>

<section class="brochure brochure--outside" aria-label="Brochure outside">
  <div class="panel panel--1">
    <div class="block block--navy" style="top:0;height:235px"></div>
    <div class="photo photo--surfer" role="img" aria-label="Photo of a woman surfing a wave on a board"></div>
    <div class="copy" style="top:22px">
      <h2 class="heading">
        <svg width="14" height="11" viewBox="0 0 16 13"><path d="M0 0H16L8 13Z" fill="var(--yellow)"/></svg>
        <span>Surfing &amp; Body<br>Boarding</span>
      </h2>
      <p>Whether its basic skills sessions included in your aquatics camp, a day surf session on the Fleurieu Peninsula or even specialized surf focused camp in the South East – we have it covered!</p>
      <p>Our surfing and body boarding sessions are definitely a popular favourite with our clients. All ages are catered for with ‘Surf Safety’ sessions for the younger ages, ‘Basic Skills’ for beginners, right through to ‘Intermediate’ and ‘Advanced’ surf specialist programs.</p>
    </div>
  </div>

  <div class="panel panel--2">
    <div class="photo photo--kayaks" role="img" aria-label="Photo of kayaks lined up on a beach at sunset"></div>
    <div class="block block--navy" style="top:260px;height:240px"></div>
    <div class="copy" style="top:318px">
      <h2 class="heading heading--center"><span>Equipment Hire</span></h2>
      <p>Going on a School camp or Personal adventure and need equipment?</p>
      <p>No problem, Harbour Lane Trips Outdoor Adventures has the equipment for you.</p>
      <p>With a large stock of equipment for all varieties of Activities we can provide equipment at an affordable price.</p>
      <p>Contact us now for more information on our Equipment and our Packaged deals.</p>
      <p>Also see our activity pages for a full range of activities that we supply equipment for.</p>
    </div>
  </div>

  <div class="panel panel--3">
    <div class="block cover-top"></div>
    <div class="brand">
      <span class="brand__mark"></span>
      <span class="brand__name">Harbour Lane<br>Trips</span>
    </div>
    <div class="photo photo--climber" role="img" aria-label="Photo of a climber abseiling down a rock face"></div>
  </div>

  <svg class="wave" viewBox="0 0 810 500" aria-hidden="true">
    <defs>
      <linearGradient id="waveOut" gradientUnits="userSpaceOnUse" x1="0" y1="0" x2="810" y2="0">
        <stop offset="0" stop-color="var(--yellow)"/>
        <stop offset=".55" stop-color="var(--lime)"/>
        <stop offset="1" stop-color="var(--green)"/>
      </linearGradient>
      <path id="curveOut" d="M-10 218 C100 210 180 228 270 245 C380 266 460 276 540 272 C640 268 720 258 820 258"/>
    </defs>
    <use href="#curveOut" transform="translate(0 13)" fill="none" stroke="var(--navy)" stroke-width="28"/>
    <use href="#curveOut" transform="translate(0 8)" fill="none" stroke="url(#waveOut)" stroke-width="16"/>
    <use href="#curveOut" transform="translate(0 27)" fill="none" stroke="var(--lime)" stroke-width="1.5"/>
  </svg>
</section>

<section class="brochure brochure--inside" aria-label="Brochure inside">
  <div class="panel panel--1">
    <div class="photo photo--cliff-group" role="img" aria-label="Photo of a school group sitting on red cliffs"></div>
    <div class="block block--navy" style="top:250px;height:250px"></div>
    <div class="copy" style="top:282px">
      <h2 class="heading">
        <svg width="14" height="11" viewBox="0 0 16 13"><path d="M0 13H16L8 0Z" fill="var(--yellow)"/></svg>
        <span>Meet the Team</span>
      </h2>
      <p>Harbour Lane Trips Outdoor Adventures is the largest provider of school camps, excursions and outdoor pursuits in South Australia and one of the largest on a national scale.</p>
      <p>Here at Harbour Lane Trips we provide outdoor experiences to schools from a junior primary level up to senior secondary.</p>
      <p>What sets us above the rest? Our school programs can be tailor made to suit the needs of your particular school, class or youth group. We can really see the importance and benefit from education in the outdoors and will design your program around the current and relevant curriculum within your school. We understand that the needs and learning outcomes of one school or group can differ immensely from another. We also service universities, businesses, youth groups, adults and special needs populations throughout South Australia and interstate.</p>
    </div>
  </div>

  <div class="panel panel--2">
    <div class="block block--navy" style="top:0;height:270px"></div>
    <div class="photo photo--beach-group" role="img" aria-label="Photo of a cheering group of students on a beach"></div>
    <div class="copy" style="top:18px">
      <h2 class="heading">
        <span>School Camps</span>
        <svg width="14" height="11" viewBox="0 0 16 13"><path d="M0 0H16L8 13Z" fill="var(--yellow)"/></svg>
      </h2>
      <p>Harbour Lane Trips offers 3 different levels of service:<br>
        <span class="levels">Level 1 – Activities Only (instructors + equipment)<br>
        Level 2 – School Camp (base level HLTOA Camp – limited provisions)<br>
        Level 3 – School Camp (All services provided)</span></p>
      <p>Organisation of learning in outdoor education<br>In order to maximise the effectiveness of any outdoor education program delivered in schools, learning should be sequential and with clearly aligned themes and specific learning outcomes. This learning can be summarised under the following organising ideas:</p>
      <ol>
        <li>1. There is a range of skills and knowledge required to be active in the outdoors.</li>
        <li>2. Individuals need to work together to achieve common goals in outdoor activities.</li>
        <li>3. Human–nature relationships enhance an individual’s experience in natural environments.</li>
        <li>4. Ecological, cultural and personal knowledge of places enhances decision making about conservation and sustainability.</li>
        <li>5. Being in nature promotes health and wellbeing.</li>
        <li>6. Journeys in natural environments promote personal growth and development</li>
      </ol>
    </div>
  </div>

  <div class="panel panel--3">
    <div class="photo photo--raft" role="img" aria-label="Photo of students paddling a raft of canoes on a river"></div>
    <div class="block block--navy" style="top:240px;height:260px"></div>
    <div class="copy" style="top:286px">
      <h2 class="heading">
        <svg width="14" height="11" viewBox="0 0 16 13"><path d="M0 13H16L8 0Z" fill="var(--yellow)"/></svg>
        <span>Kayaking &amp;<br>Canoeing</span>
      </h2>
      <p>Whether you’re after a short session of games, a basic skills session or an extended paddling journey, Harbour Lane Trips can tailor a kayaking or canoeing experience to suit. Learn to paddle according to your individual needs – whether it’s in the surf, paddling the coast, or inland on flat-water, we have a range of kayaks that can be used to suit each paddling environment. With South Australia offering such great waterways there are some great journeys and challenging environments to choose from.</p>
      <p>If you choose to undertake an extended paddling journey, participants will pack for the entire expedition and learn the basic skills of controlling the paddle craft, navigating waterways and managing a group. Participants will predominantly be paddling inland on flat-water and taking their gear for the night along with them.</p>
    </div>
  </div>

  <svg class="wave" viewBox="0 0 810 500" aria-hidden="true">
    <defs>
      <linearGradient id="waveIn" gradientUnits="userSpaceOnUse" x1="0" y1="0" x2="810" y2="0">
        <stop offset="0" stop-color="var(--yellow)"/>
        <stop offset=".5" stop-color="var(--lime)"/>
        <stop offset="1" stop-color="var(--green)"/>
      </linearGradient>
      <path id="curveIn" d="M-10 222 C120 222 180 240 270 250 C340 258 360 270 405 268 C460 266 490 256 540 252 C640 244 720 222 820 220"/>
    </defs>
    <use href="#curveIn" transform="translate(0 13)" fill="none" stroke="var(--navy)" stroke-width="28"/>
    <use href="#curveIn" transform="translate(0 8)" fill="none" stroke="url(#waveIn)" stroke-width="16"/>
    <use href="#curveIn" transform="translate(0 27)" fill="none" stroke="var(--lime)" stroke-width="1.5"/>
  </svg>
</section>

</body>
</html>
```